Electrician Business needs flyer for discount offer and advertise services

Need a promotional flyer that will grab attention,, offer:

During the months of October & November receive a 10% discount on;
Ceiling fan installation
Smoke alarm installation
Replace existing downlights for new LED downlights.
Offer expires 30th November 2016
'Keep cool, stay safe and save power with VoltMate'

Would like to advertise services and quality on reverse-side. Can have graphic pointing to reverse side on both sides, encouraging customer to read both sides of flyer.
Contact details both sides
Design to suit two-sided A5

Reverse side list services;

All residential & commercial electrical services
Electrical contracting
Real estate/strata electrical maintenance & repairs
New builds
Renovations
Security sensor lighting
Ceiling fans
Smoke Alarms
Data connections

Target Market(s)

Residential home owners and commercial, building and construction companies

Industry/Entity Type

Electrical

Font styles to use
Serif

Colors
0255a3
ffffff

Requirements
Nice to have
• A picture of a modern ceiling fan.
• Arrow/graphic pointing to reverse side, so customer reads both sides of flyer

```html
<!DOCTYPE html>
<html lang="en">
<head>
<meta charset="utf-8">
<title>VoltMate Electrical Services – Spring Discount Flyer</title>
<link rel="stylesheet" href="https://fonts.googleapis.com/css2?family=Crimson+Pro:ital,wght@0,400;0,700;1,700&display=swap">
<style>
  :root {
    --brand-blue: #0255a3;
    --deep-blue: #084f8c;
    --offer-orange: #f59c32;
    --ink: #2a1d12;
    --white: #ffffff;
    --silver-light: #f4f4f4;
    --silver-mid: #d2d2d2;
    --silver-dark: #9a9a9a;
  }
  * { margin: 0; padding: 0; box-sizing: border-box; }
  html, body { width: 846px; height: 1200px; overflow: hidden; background: var(--white); }
  .flyer {
    position: relative;
    width: 846px;
    height: 1200px;
    overflow: hidden;
    background: var(--offer-orange);
    font-family: "Crimson Pro", Georgia, serif;
    color: var(--ink);
    text-align: center;
  }

  .masthead {
    position: relative;
    height: 302px;
    background: var(--brand-blue);
    color: var(--white);
    font-weight: 700;
  }
  .masthead__name {
    position: absolute;
    left: 0; right: 0;
    top: 62px;
    font-size: 176px;
    line-height: 1;
    letter-spacing: 1px;
  }
  .masthead__tagline {
    position: absolute;
    left: 0; right: 0;
    top: 204px;
    font-size: 60px;
    line-height: 1;
    letter-spacing: 1px;
  }

  .offer { position: absolute; left: 0; right: 0; top: 320px; }
  .offer__period { font-size: 42px; font-weight: 700; line-height: 50px; }
  .offer__headline {
    color: var(--brand-blue);
    font-size: 53px;
    font-weight: 700;
    line-height: 66px;
    margin-top: 4px;
    white-space: nowrap;
  }
  .offer__headline strong {
    font-size: 77px;
    text-shadow: 2px 2px 0 var(--white), -1px -1px 0 var(--white), 1px -1px 0 var(--white), -1px 1px 0 var(--white);
  }
  .services { list-style: none; margin-top: 6px; }
  .services li {
    font-size: 46px;
    font-weight: 700;
    line-height: 46px;
    text-transform: uppercase;
    margin-bottom: 25px;
    white-space: nowrap;
  }
  .services li:last-child { margin-bottom: 0; }
  .offer__expiry { font-size: 28px; line-height: 34px; margin-top: 10px; }

  .slogan {
    position: absolute;
    left: 69px;
    top: 758px;
    width: 694px;
    height: 195px;
    border-radius: 50%;
    background: var(--deep-blue);
    border: 2px solid var(--white);
    box-shadow: 10px 10px 8px rgba(60, 30, 0, 0.55);
    display: flex;
    align-items: center;
    justify-content: center;
    color: var(--offer-orange);
    font-style: italic;
    font-weight: 700;
    font-size: 55px;
    line-height: 56px;
    white-space: nowrap;
  }

  .contact {
    position: absolute;
    left: 0;
    width: 668px;
    top: 972px;
    font-style: normal;
  }
  .contact__call { font-size: 38px; font-weight: 400; line-height: 44px; }
  .contact__line { color: var(--brand-blue); font-size: 39px; font-weight: 700; line-height: 44px; }

  .page-turn { position: absolute; right: 0; bottom: 0; width: 230px; height: 230px; }
  .page-turn svg { display: block; }
  .page-turn__label {
    position: absolute;
    right: -8px;
    bottom: 44px;
    width: 210px;
    transform: rotate(-45deg);
    font-size: 21px;
    font-weight: 700;
    line-height: 1.1;
    color: var(--ink);
    text-transform: uppercase;
  }
</style>
</head>
<body>
<main class="flyer">
  <header class="masthead">
    <h1 class="masthead__name">VoltMate</h1>
    <p class="masthead__tagline">Electrical Services</p>
  </header>

  <section class="offer">
    <p class="offer__period">During the months of October &amp; November</p>
    <h2 class="offer__headline">Receive a <strong>10% Discount</strong> on;</h2>
    <ul class="services">
      <li>Ceiling fan installation</li>
      <li>Smoke alarm installation</li>
      <li>Replace existing downlights<br>for new LED downlights.</li>
    </ul>
    <p class="offer__expiry">Offer expires 30th November 2016</p>
  </section>

  <blockquote class="slogan">‘Keep cool, stay safe and<br>save power with VoltMate’</blockquote>

  <address class="contact">
    <p class="contact__call">CONTACT US FOR MORE DETAILS!</p>
    <p class="contact__line">Daniel Harwood</p>
    <p class="contact__line">Ridgehaven NSW 2188</p>
    <p class="contact__line">0412 000 538</p>
  </address>

  <div class="page-turn">
    <svg width="230" height="230" viewBox="0 0 230 230" aria-hidden="true">
      <defs>
        <linearGradient id="curl" x1="0" y1="1" x2="1" y2="0">
          <stop offset="0" stop-color="var(--silver-dark)"/>
          <stop offset="0.4" stop-color="var(--silver-light)"/>
          <stop offset="0.7" stop-color="var(--silver-mid)"/>
          <stop offset="1" stop-color="var(--silver-dark)"/>
        </linearGradient>
      </defs>
      <path d="M230 0 L230 230 L0 230 Z" fill="var(--white)"/>
      <path d="M230 0 C190 20 140 28 100 30 C80 90 40 170 0 230 L230 230 Z" fill="url(#curl)"/>
    </svg>
    <p class="page-turn__label">See flip side<br>for more<br>info!</p>
  </div>
</main>
</body>
</html>
```